Modern business cards for a technology lab
Forge 71
Modern business cards for a technology lab - Technology Transfer
Creative Brief
Use same font as used in my logo
Be creative with different fonts around the one in the logo
Modern
Corwin Mettler
Owner
2450 West Fenmore Ave suite D Winston-Salem, NC 27139
corwinmettler@quellbox.net
People. Partnership. Progression. We want this on the front of the card with the forge 71
We are what we repeatedly do, excellence then is not an act, but a habit. -Aristotle We want the quote above on top and also the Forge 71, Inc and the People. Partnership. Progression saying.

```html
<!DOCTYPE html>
<html lang="en">
<head>
<meta charset="utf-8">
<title>Forge 71 Stationery Set</title>
<link href="https://fonts.googleapis.com/css2?family=Open+Sans:wght@400;600;700&display=swap" rel="stylesheet">
<style>
  :root {
    --bg: #ecebe8;
    --paper: #ffffff;
    --green: #6fb52c;
    --green-faint: #eef5e4;
    --green-edge: #e0edd2;
    --ink: #555555;
    --ink-soft: #8a8a8a;
    --line: #d4d4d4;
    --label: #444444;
  }
  * { box-sizing: border-box; margin: 0; padding: 0; }
  html, body { width: 1200px; height: 384px; overflow: hidden; }
  body {
    background: var(--bg);
    font-family: "Open Sans", Arial, sans-serif;
    color: var(--ink);
    position: relative;
  }

  .sheet, .envelope, .card {
    position: absolute;
    background: var(--paper);
    box-shadow: 0 2px 6px rgba(0,0,0,.22);
    overflow: hidden;
  }
  .letterhead { top: 12px; width: 240px; height: 306px; }
  .letterhead--one { left: 24px; }
  .letterhead--two { left: 300px; }
  .fax { left: 576px; top: 12px; width: 240px; height: 312px; }

  /* brand lockup: one plain circle + name */
  .brand {
    position: absolute;
    display: flex; flex-direction: column; align-items: center;
    white-space: nowrap;
  }
  .brand--row { flex-direction: row; gap: 5px; }
  .brand__mark {
    display: block; width: 18px; height: 18px; border-radius: 50%;
    background: var(--green); flex: none;
  }
  .brand__name {
    margin-top: 3px;
    font-size: 7px; font-weight: 700; color: var(--green); letter-spacing: .6px;
    line-height: 1;
  }
  .brand--row .brand__name { margin-top: 0; }

  .watermark {
    position: absolute; border-radius: 50%;
    background: radial-gradient(circle at 40% 35%, #ffffff 0%, var(--green-faint) 60%, var(--green-edge) 100%);
  }
  .contact {
    position: absolute; font-size: 5px; line-height: 7px; color: var(--ink-soft);
    white-space: nowrap;
  }
  .footer-rule { position: absolute; left: 0; right: 0; bottom: 0; height: 4px; background: var(--green); }
  .footer-line {
    position: absolute; left: 0; right: 0; bottom: 9px;
    font-size: 5px; line-height: 1; color: var(--ink-soft); text-align: center; white-space: nowrap;
  }

  /* fax form */
  .fax__title { position: absolute; left: 14px; top: 76px; font-size: 22px; font-weight: 400; color: var(--ink); line-height: 1; }
  .fax__fields {
    position: absolute; left: 14px; right: 14px; top: 108px;
    display: grid; grid-template-columns: 1fr 1fr; column-gap: 14px; row-gap: 6px;
  }
  .fax__field { font-size: 5px; line-height: 7px; border-bottom: 1px solid var(--line); }
  .fax__checks {
    position: absolute; left: 14px; right: 14px; top: 166px;
    display: flex; justify-content: space-between; font-size: 5px; line-height: 7px;
  }
  .fax__checks span::before {
    content: ""; display: inline-block; width: 6px; height: 6px;
    border: .8px solid var(--ink-soft); margin-right: 3px; vertical-align: -1px;
  }

  /* envelopes */
  .envelope--back { left: 828px; top: 64px; width: 360px; height: 84px; }
  .envelope--front { left: 828px; top: 152px; width: 360px; height: 88px; }

  /* business cards */
  .card { top: 252px; height: 96px; }
  .card--front { left: 840px; width: 156px; }
  .card--back { left: 1020px; width: 168px; }
  .card__name { display: block; font-size: 6px; font-weight: 700; color: var(--green); line-height: 8px; }
  .card__title { display: block; font-size: 5px; color: var(--ink); line-height: 7px; margin-bottom: 2px; }

  .option-label { position: absolute; top: 340px; font-size: 12px; color: var(--label); }
</style>
</head>
<body>

<section class="sheet letterhead letterhead--one">
  <div class="watermark" style="left:40px;top:72px;width:150px;height:150px;"></div>
  <div class="brand" style="left:100px;top:12px;width:40px;">
    <span class="brand__mark"></span><span class="brand__name">Forge 71</span>
  </div>
  <div class="contact" style="left:150px;top:12px;">T: 336 555 0182<br>corwinmettler@quellbox.net</div>
  <p class="footer-line">2450 West Fenmore Ave suite D Winston-Salem, NC 27139 · corwinmettler@quellbox.net</p>
  <div class="footer-rule"></div>
</section>

<section class="sheet letterhead letterhead--two">
  <div class="watermark" style="left:40px;top:72px;width:150px;height:150px;"></div>
  <div class="brand" style="left:92px;top:12px;width:40px;">
    <span class="brand__mark"></span><span class="brand__name">Forge 71</span>
  </div>
  <div class="contact" style="left:142px;top:12px;">2450 West Fenmore Ave suite D<br>Winston-Salem, NC 27139<br>T: 336 555 0182</div>
  <p class="footer-line">People. Partnership. Progression. · corwinmettler@quellbox.net</p>
  <div class="footer-rule"></div>
</section>

<section class="sheet fax">
  <div class="brand" style="left:100px;top:12px;width:40px;">
    <span class="brand__mark"></span><span class="brand__name">Forge 71</span>
  </div>
  <div class="contact" style="left:150px;top:12px;">2450 West Fenmore Ave suite D<br>Winston-Salem, NC 27139</div>
  <h1 class="fax__title">FAX</h1>
  <div class="fax__fields">
    <div class="fax__field">To:</div><div class="fax__field">From:</div>
    <div class="fax__field">Fax:</div><div class="fax__field">Pages:</div>
    <div class="fax__field">Phone:</div><div class="fax__field">Date:</div>
    <div class="fax__field">Re:</div><div class="fax__field">CC:</div>
  </div>
  <div class="fax__checks">
    <span>Urgent</span><span>Review</span><span>Comment</span><span>Reply</span><span>Recycle</span>
  </div>
  <p class="footer-line">People · Partnership · Progression</p>
  <div class="footer-rule"></div>
</section>

<div class="envelope envelope--back">
  <svg width="360" height="84" viewBox="0 0 360 84" aria-hidden="true" style="position:absolute;left:0;top:0;">
    <path d="M0 2 L180 58 L360 2" fill="none" stroke="var(--line)" stroke-width="1"/>
    <path d="M0 0 Q180 44 360 0 L360 5 Q180 50 0 5 Z" fill="var(--green)"/>
  </svg>
  <div class="brand" style="left:150px;top:44px;width:60px;">
    <span class="brand__mark" style="width:16px;height:16px;"></span><span class="brand__name">Forge 71</span>
  </div>
</div>

<div class="envelope envelope--front">
  <div class="brand" style="left:14px;top:10px;width:40px;">
    <span class="brand__mark" style="width:14px;height:14px;"></span><span class="brand__name">Forge 71</span>
  </div>
  <div class="contact" style="left:14px;top:40px;">2450 West Fenmore Ave suite D<br>Winston-Salem, NC 27139</div>
  <p class="footer-line">People · Partnership · Progression</p>
  <div class="footer-rule" style="height:3px;"></div>
</div>

<article class="card card--front">
  <div class="brand" style="left:58px;top:8px;width:40px;">
    <span class="brand__mark" style="width:12px;height:12px;"></span><span class="brand__name">Forge 71</span>
  </div>
  <div class="contact" style="left:0;right:0;top:36px;text-align:center;line-height:7px;">
    <span class="card__name">Corwin Mettler</span>
    <span class="card__title">Owner</span>
    2450 West Fenmore Ave suite D<br>Winston-Salem, NC 27139<br>corwinmettler@quellbox.net
  </div>
  <div class="footer-rule" style="height:3px;"></div>
</article>

<article class="card card--back">
  <div class="watermark" style="left:88px;top:10px;width:72px;height:72px;"></div>
  <div class="brand" style="left:14px;top:28px;width:64px;">
    <span class="brand__mark"></span><span class="brand__name">Forge 71, Inc</span>
  </div>
  <p class="footer-line">People. Partnership. Progression.</p>
  <div class="footer-rule" style="height:3px;"></div>
</article>

<p class="option-label" style="left:100px;">Option-1</p>
<p class="option-label" style="left:380px;">Option-2</p>
<p class="option-label" style="left:656px;">Option-3</p>

</body>
</html>
```